Brochure Cover and Back pages

We are a US-based cosmetics company that sells state-of-the-art skin care products, including advanced anti-aging serums, natural mineral sunscreens, organic antioxidant moisturizers, and organic face cleansers. We need a product brochure. We already have chosen a design for the layout of the product info pages. But we still need a cover page and a back page. We are looking for simple but elegant design for the cover page. The back page is less important and we already know what we want on the back page. It will be the company's mission statement and at the bottom, the company URL, phone number, etc.

The brochure has two folds. So there will be three panels on both sides. The size of each panel is 16.5 (l) x 9.5 (w) cm.

At the end of the project, we expect the designer to integrate all the pages so that the finished copy is read to be sent off to a printing service for printing.

All the product info pages are attached. Also attached are the text (info) to go on the back page, company logo with and without the tagline, the icon in the logo.

YOu are welcome to visit our website www.corvanyx.com to learn about our products.

Industry/Entity Type

Cosmetics

```html
<!DOCTYPE html>
<html lang="en">
<head>
<meta charset="utf-8">
<title>Corvanyx Brochure – Back and Cover Panels</title>
<link rel="stylesheet" href="https://fonts.googleapis.com/css2?family=Montserrat:wght@300;400;500;600;700&display=swap">
<style>
  :root {
    --bg: #ededed;
    --paper: #ffffff;
    --ink: #111111;
    --teal: #00a3c0;
    --blue: #1f7be6;
    --shadow: rgba(0, 0, 0, 0.18);
  }
  * { box-sizing: border-box; margin: 0; padding: 0; }
  html, body {
    width: 1200px;
    height: 966px;
    overflow: hidden;
    background: radial-gradient(circle at 50% 45%, #ffffff 0%, var(--bg) 80%);
    font-family: "Montserrat", sans-serif;
    color: var(--ink);
  }
  .spread {
    position: absolute;
    left: 160px;
    top: 100px;
    width: 880px;
    height: 766px;
    display: flex;
    box-shadow: 0 6px 24px var(--shadow);
  }
  .panel {
    position: relative;
    width: 440px;
    height: 766px;
    background: var(--paper);
    overflow: hidden;
  }
  .panel--back { border-right: 1px solid #e2e2e2; }

  /* Back panel */
  .back-brand {
    position: absolute;
    top: 150px;
    left: 0;
    width: 100%;
    display: flex;
    align-items: center;
    justify-content: center;
    gap: 14px;
    font-weight: 600;
    font-size: 46px;
    color: var(--teal);
  }
  .back-brand__dot {
    width: 22px;
    height: 22px;
    border-radius: 50%;
    background: var(--teal);
  }
  .contact {
    position: absolute;
    top: 420px;
    left: 0;
    width: 100%;
    text-align: center;
  }
  .contact__title {
    font-weight: 600;
    font-size: 27px;
    letter-spacing: 0.5px;
  }
  .contact__heading {
    font-weight: 600;
    font-size: 16px;
    margin-top: 44px;
  }
  .contact__line {
    font-weight: 400;
    font-size: 15.5px;
    line-height: 1.35;
  }
  .contact__line--phone { font-size: 14px; margin-top: 8px; }

  /* Front panel */
  .brand {
    position: absolute;
    top: 38px;
    left: 22px;
    font-weight: 700;
    font-size: 58px;
    letter-spacing: -1px;
    color: var(--ink);
  }
  .tagline {
    position: absolute;
    top: 112px;
    left: 62px;
    font-weight: 400;
    font-size: 17px;
    letter-spacing: 0.5px;
    color: #333;
  }
  .pixel-band {
    position: absolute;
    top: 150px;
    left: 0;
    width: 100%;
    height: 190px;
    background: linear-gradient(90deg,
      #f05a28 0%, #f7b21b 18%, #e8e21a 32%, #7bc943 45%,
      #34b7c9 58%, #3a6fd8 72%, #7a3fc9 86%, #e0218a 100%);
    -webkit-mask: linear-gradient(180deg, transparent 0%, #000 25%, #000 70%, transparent 100%);
            mask: linear-gradient(180deg, transparent 0%, #000 25%, #000 70%, transparent 100%);
    opacity: 0.85;
  }
  .headline {
    position: absolute;
    top: 378px;
    left: 14px;
    font-size: 29px;
    line-height: 1.22;
    font-weight: 300;
  }
  .headline__accent { color: var(--blue); font-weight: 700; }
  .headline__strong { font-weight: 700; }
  .front-brand {
    position: absolute;
    top: 428px;
    right: 14px;
    display: flex;
    align-items: center;
    gap: 8px;
    font-weight: 600;
    font-size: 17px;
    color: var(--teal);
  }
  .front-brand__dot {
    width: 12px;
    height: 12px;
    border-radius: 50%;
    background: var(--teal);
  }
  .products {
    position: absolute;
    top: 500px;
    left: 20px;
    width: 400px;
    height: 150px;
    border-radius: 6px;
    background: linear-gradient(180deg, #ffffff 0%, #eef0f2 60%, #d9dde1 100%);
  }
  .website-bar {
    position: absolute;
    bottom: 0;
    left: 0;
    width: 100%;
    height: 78px;
    background: var(--teal);
    color: #fff;
    font-size: 15px;
    font-weight: 400;
    display: flex;
    align-items: center;
    justify-content: center;
    padding-top: 14px;
  }
  .website-bar::before {
    content: "";
    position: absolute;
    top: 0;
    left: 0;
    width: 100%;
    height: 22px;
    background: var(--paper);
  }
</style>
</head>
<body>
  <main class="spread">
    <section class="panel panel--back">
      <div class="back-brand">
        <span class="back-brand__dot"></span>
        <span>Corvanyx</span>
      </div>
      <div class="contact">
        <h2 class="contact__title">CUSTOMER SERVICE</h2>
        <p class="contact__line contact__line--phone">1-855-5-CORVAN (855-552-6782)</p>
        <h3 class="contact__heading">ADDRESS</h3>
        <p class="contact__line">2150 Larkmoor Ave.&nbsp; Suite 400</p>
        <p class="contact__line">Fairhaven, CA 94087</p>
        <h3 class="contact__heading">WEBSITE</h3>
        <p class="contact__line">www.Corvanyx.com</p>
      </div>
    </section>

    <section class="panel panel--front">
      <h1 class="brand">Corvanyx</h1>
      <p class="tagline">Bringing You Smart Skin Care</p>
      <div class="pixel-band" role="img" aria-label="Colourful wave of small squares and soft bubbles in rainbow tones"></div>
      <p class="headline">
        Creating<br>
        <span class="headline__accent">Beauty solutions</span><br>
        through <span class="headline__strong">Science</span>
      </p>
      <div class="front-brand">
        <span class="front-brand__dot"></span>
        <span>Corvanyx</span>
      </div>
      <div class="products" role="img" aria-label="Photo of four skin care products: a bottle, a tube, a pump serum and a cream jar"></div>
      <div class="website-bar">Website: www.corvanyx.com</div>
    </section>
  </main>
</body>
</html>
```